3 Flyer Project: Industrial, Civil, and Commercial

Total of 3 separate flyers that go together to be put in folders for marketing. The three flyer categories will be Industrial, Civil, and Commercial. I will upload three photos for each flyer and verbiage for each flyer. The photos may change upon final revisions. We want creativity and not just bullet points on a page.

FLYER #1 INDUSTRIAL

INDUSTRIAL EXPERIENCE:
BRELLANT COMPANY
VESKAR
OAKMOOR PIT MINE
GALDWYN FORGE STEEL
PERNOTH QUARTZWORKS
DUNMARROW VALE LOOP RAILWAY

INDUSTRIAL FOCUS AREAS:
PLANT FACILITY WATER SYSTEMS
HEAVY CONCRETE
FACILITY REPAIR
INDUSTRIAL UPGRADES
RAILWAYS AND MANUFACTURING

INDUSTRIAL SOLUTIONS:
WE MAINTAIN AN EXTENSIVE LEVEL OF DETAIL AND INNOVATIVE PROBLEM-SOLVING TALENTS TO DELIVER HIGH QUALITY, SUSTAINABLE SOLUTIONS.

FLYER #2 CIVIL

CIVIL EXPERIENCE:
VELDORAN DEPT. OF TRANSPORTATION
KESTRIA DEPT. OF TRANSPORTATION
PLOVENDA DEPT. OF TRANSPORTATION
BUREAU OF WORKSMITHS
NATIONAL SKYWAYS AUTHORITY BOARD
MINISTRY OF GUARDIANSHIP

CIVIL FOCUS AREAS:
AIRFIELD
STREETSCAPES
STORM DRAINAGE
UTILITY UPGRADES
BOX CULVERTS
RETAINING WALLS

CIVIL SOLUTIONS:
WE SPECIALIZE IN COMPLEX CIVIL PROJECTS.

FLYER #3 COMMERCIAL

COMMERCIAL EXPERIENCE:
HOLLENBRAKE UPLANDS UNIVERSITY
VELDORAN OFFICE OF STRUCTURES
TOWN OF BRANWICK, MISSISSIPPI
TOWN OF MERRODA, MISSISSIPPI
ACADEMY FOR ADVANCED STUDIES

COMMERCIAL FOCUS AREAS:
NEW CONSTRUCTION
RENOVATIONS
STRUCTURAL FOUNDATIONS
STRUCTURAL UPGRADES

COMMERCIAL SOLUTIONS:
WE NOT ONLY KNOW HOW ALL THE PARTS AND PIECES FIT TOGETHER WITHIN A PROJECT, BUT WE SPECIALIZE IN THE SELF PERFORMANCE OF MANY DIVISIONS WHICH DIFFERENTIATES US FROM MANY OTHER GENERAL CONTRACTORS.

Marketing

• 3 photos on each flyer based on the Industrial, Commercial, and Civil flyers description. Our company logo as well as descriptions shown for each flyer. The blue we use in our logo cmyk is 100-80-0-22

```html
<!DOCTYPE html>
<html lang="en">
<head>
<meta charset="utf-8">
<title>Halverd Construction – Solutions Flyers</title>
<link href="https://fonts.googleapis.com/css2?family=Oswald:wght@500;600&family=Lato:wght@400;700&display=swap" rel="stylesheet">
<style>
  :root {
    --brand-blue: #263b85;
    --brand-blue-dark: #1d2f6e;
    --ink: #1b1b1b;
    --paper: #ffffff;
    --paper-tint: #eef0f8;
    --stage: #cdcdcd;
  }
  * { box-sizing: border-box; margin: 0; padding: 0; }
  html, body { width: 1200px; height: 1200px; overflow: hidden; }
  body { background: var(--stage); position: relative; font-family: "Lato", sans-serif; }

  .flyer {
    position: absolute;
    width: 393px; height: 557px;
    background: linear-gradient(135deg, var(--paper) 0%, var(--paper) 60%, var(--paper-tint) 100%);
    overflow: hidden;
  }
  .flyer--industrial { left: 726px; top: 80px; z-index: 1; }
  .flyer--civil { left: 375px; top: 283px; z-index: 2; }
  .flyer--commercial { left: 86px; top: 555px; z-index: 3; }

  .brand {
    position: absolute; top: 0; left: 0; width: 100%; height: 70px;
    display: flex; align-items: center; justify-content: center; gap: 7px;
  }
  .brand__square { width: 24px; height: 24px; background: var(--brand-blue); }
  .brand__name {
    font-family: "Oswald", sans-serif; font-weight: 600;
    color: var(--brand-blue); font-size: 20px; letter-spacing: 0.5px; line-height: 1;
  }

  .photo {
    position: absolute; top: 70px; left: 0; width: 100%; height: 202px;
  }
  .photo--industrial { background: linear-gradient(180deg, #c9ced6 0%, #9ba3ad 55%, #7d7f73 100%); }
  .photo--civil { background: linear-gradient(180deg, #b9c7d8 0%, #dfe3e8 50%, #c2c3c1 100%); }
  .photo--commercial { background: linear-gradient(180deg, #8fb3dd 0%, #9d4b3a 55%, #b98a5c 100%); }

  .frame-blue-h { position: absolute; top: 70px; left: 0; width: 98px; height: 10px; background: var(--brand-blue); }
  .frame-blue-v { position: absolute; top: 70px; left: 0; width: 16px; height: 100px; background: var(--brand-blue); }
  .frame-white-h { position: absolute; top: 260px; right: 0; width: 98px; height: 12px; background: var(--paper); }
  .frame-white-v { position: absolute; top: 172px; right: 0; width: 16px; height: 100px; background: var(--paper); }

  .banner {
    position: absolute; top: 272px; left: 0; width: 100%; height: 84px;
    background: var(--brand-blue); color: var(--paper);
    text-align: center; padding: 10px 40px 0;
  }
  .banner__title {
    font-family: "Oswald", sans-serif; font-weight: 500;
    font-size: 29px; letter-spacing: 1px; line-height: 1.1;
  }
  .banner__text { font-size: 7.6px; font-weight: 700; line-height: 1.25; margin-top: 5px; }
  .banner__text--caps { text-transform: uppercase; }

  .column { position: absolute; top: 378px; width: 170px; }
  .column--left { left: 46px; }
  .column--right { left: 212px; }
  .column__heading {
    font-family: "Oswald", sans-serif; font-weight: 600;
    font-size: 13px; color: var(--ink); letter-spacing: 0.2px;
    display: inline-block; padding-bottom: 3px;
    border-bottom: 3px solid var(--ink);
  }
  .column__list { list-style: none; margin-top: 14px; }
  .column__list li {
    font-size: 8px; line-height: 14px; color: var(--ink);
    padding-left: 16px; position: relative; white-space: nowrap;
  }
  .column__list--bold li { font-weight: 700; }
  .column__list li::before {
    content: ""; position: absolute; left: 0; top: 4.5px;
    width: 5px; height: 5px; border: 1.2px solid var(--brand-blue);
  }

  .footer {
    position: absolute; bottom: 0; left: 0; width: 100%; height: 24px;
    background: var(--brand-blue);
  }
  .contact {
    position: absolute; bottom: 0; width: 110px; height: 38px;
    display: flex; flex-direction: column; align-items: center;
  }
  .contact--phone { left: 7px; }
  .contact--mail { left: 141px; }
  .contact--web { left: 272px; }
  .contact__icon {
    width: 14px; height: 14px; background: var(--brand-blue);
    border: 1.5px solid var(--paper);
    display: flex; align-items: center; justify-content: center;
  }
  .contact__text { color: var(--paper); font-size: 6.4px; font-weight: 700; margin-top: 6px; letter-spacing: 0.2px; }
</style>
</head>
<body>

<svg width="0" height="0" style="position:absolute">
  <defs>
    <symbol id="icon-phone" viewBox="0 0 10 10"><path d="M2.2 1 L3.6 1 L4.2 3 L3.3 3.7 C3.8 4.9 5 6.1 6.3 6.7 L7 5.8 L9 6.4 L9 7.8 C9 8.5 8.5 9 7.8 9 C4.2 8.7 1.3 5.8 1 2.2 C1 1.5 1.5 1 2.2 1 Z" fill="#fff"/></symbol>
    <symbol id="icon-mail" viewBox="0 0 10 10"><rect x="1" y="2.2" width="8" height="5.6" fill="#fff"/><polyline points="1,2.4 5,5.6 9,2.4" fill="none" stroke="#263b85" stroke-width="0.8"/></symbol>
    <symbol id="icon-web" viewBox="0 0 10 10"><circle cx="5" cy="5" r="3.8" fill="none" stroke="#fff" stroke-width="0.9"/><ellipse cx="5" cy="5" rx="1.6" ry="3.8" fill="none" stroke="#fff" stroke-width="0.8"/><line x1="1.2" y1="5" x2="8.8" y2="5" stroke="#fff" stroke-width="0.8"/></symbol>
  </defs>
</svg>

<!-- Industrial -->
<section class="flyer flyer--industrial">
  <header class="brand"><span class="brand__square"></span><span class="brand__name">HALVERD CONSTRUCTION</span></header>
  <div class="photo photo--industrial" role="img" aria-label="Power plant with tall smokestacks and cooling towers under a cloudy sky"></div>
  <div class="frame-blue-h"></div><div class="frame-blue-v"></div>
  <div class="frame-white-h"></div><div class="frame-white-v"></div>
  <div class="banner">
    <h1 class="banner__title">INDUSTRIAL SOLUTIONS</h1>
    <p class="banner__text">We Maintain An Extensive Level Of Detail And Innovative Problem Solving<br>Talents To Deliver Highquality, Sustainable Solutions.</p>
  </div>
  <div class="column column--left">
    <h2 class="column__heading">INDUSTRIAL EXPERIENCE</h2>
    <ul class="column__list column__list--bold">
      <li>Brellant Company</li><li>Veskar</li><li>Oakmoor Pit Mine</li>
      <li>Galdwyn Forge Steel</li><li>Pernoth Quartzworks</li><li>Dunmarrow Vale Loop Railway</li>
    </ul>
  </div>
  <div class="column column--right">
    <h2 class="column__heading">INDUSTRIAL FOCUS AREAS</h2>
    <ul class="column__list column__list--bold">
      <li>Plant Facility Water Systems</li><li>Heavy Concrete</li><li>Facility Repair</li>
      <li>Industrial Upgrades</li><li>Railways And Manufacturing</li>
    </ul>
  </div>
  <footer class="footer"></footer>
  <div class="contact contact--phone"><span class="contact__icon"><svg width="9" height="9"><use href="#icon-phone"/></svg></span><span class="contact__text">+123 456 7890</span></div>
  <div class="contact contact--mail"><span class="contact__icon"><svg width="9" height="9"><use href="#icon-mail"/></svg></span><span class="contact__text">info@halverd.com</span></div>
  <div class="contact contact--web"><span class="contact__icon"><svg width="9" height="9"><use href="#icon-web"/></svg></span><span class="contact__text">www.halverd.com</span></div>
</section>

<!-- Civil -->
<section class="flyer flyer--civil">
  <header class="brand"><span class="brand__square"></span><span class="brand__name">HALVERD CONSTRUCTION</span></header>
  <div class="photo photo--civil" role="img" aria-label="Jet airliners parked on an airfield apron"></div>
  <div class="frame-blue-h"></div><div class="frame-blue-v"></div>
  <div class="frame-white-h"></div><div class="frame-white-v"></div>
  <div class="banner">
    <h1 class="banner__title">CIVIL SOLUTIONS</h1>
    <p class="banner__text banner__text--caps">We specialize in complex civil projects</p>
  </div>
  <div class="column column--left">
    <h2 class="column__heading">CIVIL EXPERIENCE</h2>
    <ul class="column__list">
      <li>Veldoran dept. Of transportation</li><li>Kestria dept. Of transportation</li>
      <li>Plovenda dept. Of transportation</li><li>Bureau of worksmiths</li>
      <li>National skyways authority board</li><li>Ministry of guardianship</li>
    </ul>
  </div>
  <div class="column column--right">
    <h2 class="column__heading">INDUSTRIAL FOCUS AREAS</h2>
    <ul class="column__list column__list--bold">
      <li>Airfield</li><li>Streetscapes</li><li>Storm drainage</li>
      <li>Utility upgrades</li><li>Box culverts</li><li>Retaining walls</li>
    </ul>
  </div>
  <footer class="footer"></footer>
  <div class="contact contact--phone"><span class="contact__icon"><svg width="9" height="9"><use href="#icon-phone"/></svg></span><span class="contact__text">+123 456 7890</span></div>
  <div class="contact contact--mail"><span class="contact__icon"><svg width="9" height="9"><use href="#icon-mail"/></svg></span><span class="contact__text">info@halverd.com</span></div>
  <div class="contact contact--web"><span class="contact__icon"><svg width="9" height="9"><use href="#icon-web"/></svg></span><span class="contact__text">www.halverd.com</span></div>
</section>

<!-- Commercial -->
<section class="flyer flyer--commercial">
  <header class="brand"><span class="brand__square"></span><span class="brand__name">HALVERD CONSTRUCTION</span></header>
  <div class="photo photo--commercial" role="img" aria-label="Red brick multi-storey building under renovation with construction equipment"></div>
  <div class="frame-blue-h"></div><div class="frame-blue-v"></div>
  <div class="frame-white-h"></div><div class="frame-white-v"></div>
  <div class="banner">
    <h1 class="banner__title">COMMERCIAL SOLUTIONS</h1>
    <p class="banner__text banner__text--caps">We not only know how all the parts and pieces fit together<br>within a project, but we specialize in theself performance of<br>many divisions which differentiates us from many other general<br>contractors</p>
  </div>
  <div class="column column--left">
    <h2 class="column__heading">COMMERCIAL EXPERIENCE</h2>
    <ul class="column__list">
      <li>Hollenbrake uplands university</li><li>Veldoran office of structures</li>
      <li>Town of branwick, mississippi</li><li>Town of merroda, mississippi</li>
      <li>Academy for advanced studies</li>
    </ul>
  </div>
  <div class="column column--right">
    <h2 class="column__heading">COMMERCIAL FOCUS AREAS</h2>
    <ul class="column__list">
      <li>New construction</li><li>Renovations</li>
      <li>Structural foundations</li><li>Structural upgrades</li>
    </ul>
  </div>
  <footer class="footer"></footer>
  <div class="contact contact--phone"><span class="contact__icon"><svg width="9" height="9"><use href="#icon-phone"/></svg></span><span class="contact__text">+123 456 7890</span></div>
  <div class="contact contact--mail"><span class="contact__icon"><svg width="9" height="9"><use href="#icon-mail"/></svg></span><span class="contact__text">info@halverd.com</span></div>
  <div class="contact contact--web"><span class="contact__icon"><svg width="9" height="9"><use href="#icon-web"/></svg></span><span class="contact__text">www.halverd.com</span></div>
</section>

</body>
</html>
```